Quillory Points website re-design and

the institute of massage therapy is ready for a new website. The current website is around 12 years old and it looks old. Luckily the clients is not against changing the colors so the new design does not have to use the current ugly green color scheme. Be creative! Make it pretty, modern and inviting. The current colors look like mold. Nobody likes mold. I have attached the logo asset file as well as a txt document that details the new website design parameters

1 page

```html
<!DOCTYPE html>
<html lang="en">
<head>
<meta charset="utf-8">
<title>Quillory Points Institute</title>
<link rel="stylesheet" href="https://fonts.googleapis.com/css2?family=Oswald:wght@400;600&family=Quicksand:wght@400;500;700&family=Open+Sans:wght@400;600;700&display=swap">
<style>
:root{
  --orange:#f7941d;
  --blue:#1a9fd6;
  --ink:#2b2b2b;
  --muted:#7d7d7d;
  --sky:#eaf6fc;
  --ring:#d4eefa;
  --teal:#c9f0ee;
  --mist:#f4f7f9;
  --footer:#333333;
  --white:#ffffff;
}
*{box-sizing:border-box;margin:0;padding:0}
html,body{width:1200px;height:4412px;overflow:hidden}
body{position:relative;background:var(--white);font-family:"Open Sans",sans-serif;color:var(--ink)}
.abs{position:absolute}
.btn{position:absolute;background:var(--orange);color:var(--white);font:700 13px "Open Sans",sans-serif;display:flex;align-items:center;justify-content:center;letter-spacing:.3px;box-shadow:0 3px 8px rgba(247,148,29,.25)}
.section-title{position:absolute;left:0;width:1200px;text-align:center;font-family:"Quicksand",sans-serif;font-weight:500;color:var(--blue)}
.tick{position:absolute;width:20px;height:18px}
.photo{position:absolute}

/* header / hero */
.hero-photo{left:0;top:0;width:1200px;height:800px;background:linear-gradient(100deg,#f1ebe6 0%,#ece2da 35%,#d8bba4 60%,#b88d72 80%,#e9dcd2 100%)}
.logo{position:absolute;font:600 18px "Open Sans",sans-serif;color:var(--ink);letter-spacing:.5px}
.nav{position:absolute;left:624px;top:40px;display:flex;gap:24px;font:400 11px "Open Sans",sans-serif;color:var(--white)}
.hero-title{left:163px;top:166px;font-family:"Oswald",sans-serif;font-size:50px;line-height:64px;color:var(--ink);font-weight:400}
.hero-title b{font-weight:600}
.hero-text{left:163px;top:312px;width:360px;font-size:18px;line-height:25px}
.search-label{left:163px;top:402px;font:600 15px "Open Sans",sans-serif}
.field{position:absolute;left:163px;width:320px;height:42px;background:rgba(255,255,255,.75);border:1px solid #e6dcd4;font-size:11px;color:#888;padding-left:26px;display:flex;align-items:center}

/* cards */
.card{position:absolute;top:976px;width:267px;height:346px;background:var(--white);box-shadow:0 4px 16px rgba(0,0,0,.12);text-align:center}
.card .photo{left:0;top:0;width:267px;height:188px}
.card h3{position:absolute;top:206px;width:100%;font:600 16px "Open Sans",sans-serif}
.card p{position:absolute;top:242px;left:22px;right:22px;font-size:11px;line-height:18px;color:var(--muted)}
.card .more{position:absolute;top:308px;width:100%;font:600 11px "Open Sans",sans-serif;color:var(--orange)}

/* about */
.about-list{position:absolute;left:218px;top:1562px;width:520px;list-style:none;font-size:14px;line-height:22px}
.about-list li{position:absolute;left:48px;width:520px}

/* shop */
.shop-band{left:0;top:1934px;width:1200px;height:389px;background:var(--sky)}
.shop-item{position:absolute;font-size:14.5px}

/* certs */
.cert{position:absolute;top:2500px;width:274px;height:311px;background:var(--white);box-shadow:0 4px 16px rgba(0,0,0,.07);text-align:center}
.cert .badge{position:absolute;left:90px;top:46px;width:96px;height:74px;background:#d9cfb7;border:3px solid #b8a98b}
.cert h3{position:absolute;top:138px;width:100%;font:600 16px/20px "Open Sans",sans-serif}
.cert p{position:absolute;top:186px;left:40px;right:40px;font-size:12.5px;line-height:21px;color:var(--muted)}
.cert .more{position:absolute;top:242px;width:100%;font:600 11px "Open Sans",sans-serif;color:var(--orange)}

/* faq */
.faq{position:absolute;width:355px}
.faq .q-icon{position:absolute;left:0;top:2px;width:26px;height:26px;border:1.5px solid var(--orange);border-radius:50%;color:var(--orange);font:600 14px "Open Sans",sans-serif;display:flex;align-items:center;justify-content:center}
.faq h4{position:absolute;left:42px;top:0;width:320px;font:600 11.5px/14px "Open Sans",sans-serif}
.faq p{position:absolute;left:42px;width:320px;font-size:10.5px;line-height:17px;color:var(--muted)}
.faq-rule{position:absolute;height:1px;background:#e5e5e5}

/* footer */
.footer{left:0;top:4131px;width:1200px;height:281px;background:var(--footer)}
.flink{position:absolute;color:var(--white);font-size:15px}
</style>
</head>
<body>

<!-- HERO -->
<div class="photo hero-photo abs" role="img" aria-label="Woman relaxing on a massage table receiving a head massage, towel under her neck"></div>
<svg class="abs" style="left:0;top:700px" width="1200" height="110" viewBox="0 0 1200 110">
  <path d="M0 40 C120 -10 260 10 420 30 C620 55 800 120 1000 80 C1100 60 1160 30 1200 20 L1200 110 L0 110 Z" fill="#ffffff"/>
</svg>
<div class="logo" style="left:56px;top:46px">Quillory Points Institute</div>
<nav class="nav"><span>Home</span><span>Courses ▾</span><span>Guidelines</span><span>FAQs</span><span>Policies</span><span>About</span></nav>
<div class="btn" style="left:1007px;top:27px;width:133px;height:48px;font-size:15px">LOGIN</div>

<h1 class="abs hero-title">The most <b>trusted</b><br>name in massage</h1>
<p class="abs hero-text">Lorem ipsum dolor sit amet, consectetuer adipiscing elit, sed diam nonummy nibh</p>
<div class="abs search-label">SEARCH ONLINE COURSES</div>
<div class="field" style="top:435px">Search By Keyboard</div>
<div class="field" style="top:488px">Number Of CE Hours
  <svg class="abs" style="right:18px;top:17px" width="10" height="7" viewBox="0 0 10 7"><path d="M1 1l4 4 4-4" stroke="#888" fill="none" stroke-width="1.4"/></svg>
</div>
<div class="btn" style="left:168px;top:560px;width:140px;height:46px">SEARCH</div>

<!-- POPULAR COURSES -->
<h2 class="section-title" style="top:842px;font-size:33px">Our Most Popular Courses</h2>
<p class="abs" style="left:0;top:900px;width:1200px;text-align:center;font-size:12.5px;line-height:22px;color:var(--muted)">Lorem ipsum dolor sit amet, consectetuer adipiscing elit, sed diam nonummy nibh<br>euismod tincidunt ut laoreet dolore magna aliquam</p>

<svg class="abs" style="left:0;top:1010px" width="1200" height="430" viewBox="0 0 1200 430">
  <path d="M0 12 A200 200 0 0 1 200 210 A200 200 0 0 1 0 400 L0 345 A140 140 0 0 0 140 210 A140 140 0 0 0 0 72 Z" fill="var(--ring)"/>
  <path d="M1200 60 A220 220 0 0 0 878 250 L950 260 A150 150 0 0 1 1200 130 Z" fill="var(--teal)"/>
</svg>

<div class="card" style="left:161px">
  <div class="photo" style="background:linear-gradient(135deg,#d9c2ae,#efe4da 60%,#cbb3a0)" role="img" aria-label="Therapist giving a prenatal massage to a pregnant client"></div>
  <h3>Pregnancy / Doula</h3>
  <p>Courses and packages to become certified in every stage of childbearing, from infertility to infant massage</p>
  <div class="more">FIND OUT MORE</div>
</div>
<div class="card" style="left:466px">
  <div class="photo" style="background:radial-gradient(circle at 50% 55%,#f2b24a,#a2441a 55%,#3e130a)" role="img" aria-label="Lit candles and spa stones in warm light"></div>
  <h3>Florida Laws &amp; Packages</h3>
  <p>Courses and packages required to obtain, reinstate, or renew your Florida massage therapy license</p>
  <div class="more">FIND OUT MORE</div>
</div>
<div class="card" style="left:770px">
  <div class="photo" style="background:linear-gradient(135deg,#6f675f,#b7ada2 55%,#e3ddd6)" role="img" aria-label="Woman studying at a laptop in a home office"></div>
  <h3>Research Courses</h3>
  <p>Courses approved by the NBQLT to earn mandated research hours for Board Certification renewal</p>
  <div class="more">FIND OUT MORE</div>
</div>

<!-- ABOUT -->
<div class="photo" style="left:-40px;top:1430px;width:225px;height:445px;border-radius:0 50% 50% 0 / 0 50% 50% 0;background:linear-gradient(160deg,#e9ecef,#d6cfc8 60%,#b9a597)" role="img" aria-label="Beautician in gloves giving a facial treatment"></div>
<div class="photo" style="left:807px;top:1401px;width:366px;height:366px;border-radius:50%;background:linear-gradient(140deg,#f2f2f2,#d9dcdf 50%,#8aa8c9)" role="img" aria-label="Therapist massaging a client seated in a massage chair"></div>
<svg class="abs" style="left:1120px;top:1490px" width="80" height="260" viewBox="0 0 80 260"><path d="M0 0 A130 130 0 0 1 0 260 L0 230 A100 100 0 0 0 0 30 Z" fill="var(--teal)"/></svg>

<div class="abs" style="left:219px;top:1400px;font-size:17px;color:#444">About us</div>
<h2 class="abs" style="left:218px;top:1426px;font:500 40px 'Quicksand',sans-serif;color:var(--blue)">The Quillory Points Institute</h2>
<p class="abs" style="left:219px;top:1486px;width:520px;font:600 17px/26px 'Open Sans',sans-serif">Ut wisi enim ad minim veniam, quis nostrud exerci aliq uip tation ullamcorper suscipit lobortis nisl</p>

<ul class="about-list">
  <li style="top:0">Duis autem vel eum iriure dolor in hendrerit in vulputate velit</li>
  <li style="top:38px">Quis nostrud exerci tation ullamcorper suscipit lobortis nisl ut aliq ui ex ea commodo consequat.</li>
  <li style="top:100px">Duis autem vel eum iriure dolor in hendrerit in vulputate velit esse molestie consequat vel illum.</li>
  <li style="top:160px">Sed diam nonummy nibh euismod tincidunt ut laoreet dolore magna</li>
  <li style="top:197px">Quis nostrud exerci tation ullamcorper suscipit</li>
</ul>
<svg class="tick" style="left:218px;top:1567px" viewBox="0 0 20 18"><path d="M2 9l5 6L18 2" stroke="var(--blue)" stroke-width="3" fill="none"/></svg>
<svg class="tick" style="left:218px;top:1605px" viewBox="0 0 20 18"><path d="M2 9l5 6L18 2" stroke="var(--blue)" stroke-width="3" fill="none"/></svg>
<svg class="tick" style="left:218px;top:1667px" viewBox="0 0 20 18"><path d="M2 9l5 6L18 2" stroke="var(--blue)" stroke-width="3" fill="none"/></svg>
<svg class="tick" style="left:218px;top:1727px" viewBox="0 0 20 18"><path d="M2 9l5 6L18 2" stroke="var(--blue)" stroke-width="3" fill="none"/></svg>
<svg class="tick" style="left:218px;top:1764px" viewBox="0 0 20 18"><path d="M2 9l5 6L18 2" stroke="var(--blue)" stroke-width="3" fill="none"/></svg>
<div class="btn" style="left:217px;top:1806px;width:141px;height:48px">READ MORE</div>

<!-- SHOP -->
<div class="abs shop-band"></div>
<div class="photo" style="left:840px;top:1934px;width:360px;height:389px;background:linear-gradient(90deg,rgba(234,246,252,1),#efe2d8 35%,#e4cbb9 75%,#f3ece6)" role="img" aria-label="Woman with towel-wrapped hair touching her face"></div>
<div class="photo" style="left:5px;top:2150px;width:240px;height:165px;background:radial-gradient(ellipse at 45% 60%,#b79879,#dacbb9 45%,rgba(234,246,252,0) 72%)" role="img" aria-label="Oil bottle, stacked spa stones and bath salt"></div>
<h2 class="section-title" style="top:2012px;font-size:33px;left:-77px">Shop Our Courses</h2>
<div class="shop-item" style="left:258px;top:2085px">Certified Fertility Massage Therapist</div>
<div class="shop-item" style="left:258px;top:2125px">Anatomy Fascial Lines</div>
<div class="shop-item" style="left:258px;top:2165px">Deep Tissue Therapy</div>
<div class="shop-item" style="left:258px;top:2209px">Ethics - Listening</div>
<div class="shop-item" style="left:589px;top:2085px">Pathology - Deep Vein Thrombosis</div>
<div class="shop-item" style="left:589px;top:2125px">Aromatherapy for Massage</div>
<div class="shop-item" style="left:589px;top:2165px">Ethics - Professionalism</div>
<svg class="tick" style="left:222px;top:2088px" viewBox="0 0 20 18"><path d="M2 9l5 6L18 2" stroke="var(--blue)" stroke-width="3" fill="none"/></svg>
<svg class="tick" style="left:222px;top:2128px" viewBox="0 0 20 18"><path d="M2 9l5 6L18 2" stroke="var(--blue)" stroke-width="3" fill="none"/></svg>
<svg class="tick" style="left:222px;top:2168px" viewBox="0 0 20 18"><path d="M2 9l5 6L18 2" stroke="var(--blue)" stroke-width="3" fill="none"/></svg>
<svg class="tick" style="left:222px;top:2212px" viewBox="0 0 20 18"><path d="M2 9l5 6L18 2" stroke="var(--blue)" stroke-width="3" fill="none"/></svg>
<svg class="tick" style="left:552px;top:2088px" viewBox="0 0 20 18"><path d="M2 9l5 6L18 2" stroke="var(--blue)" stroke-width="3" fill="none"/></svg>
<svg class="tick" style="left:552px;top:2128px" viewBox="0 0 20 18"><path d="M2 9l5 6L18 2" stroke="var(--blue)" stroke-width="3" fill="none"/></svg>
<svg class="tick" style="left:552px;top:2168px" viewBox="0 0 20 18"><path d="M2 9l5 6L18 2" stroke="var(--blue)" stroke-width="3" fill="none"/></svg>
<div class="btn" style="left:556px;top:2215px;width:141px;height:48px">VIEW MORE</div>

<!-- CERTIFICATIONS -->
<div class="abs" style="left:0;top:2323px;width:1200px;height:437px;background:var(--mist)"></div>
<h2 class="abs" style="left:159px;top:2406px;font:500 32px 'Quicksand',sans-serif;color:var(--blue)">Our Certifications</h2>
<svg class="abs" style="left:128px;top:2628px" width="90" height="20" viewBox="0 0 90 20">
  <path d="M30 10H2M10 3L2 10l8 7" stroke="#9a9a9a" stroke-width="1.6" fill="none"/>
  <path d="M55 10h28M75 3l8 7-8 7" stroke="#9a9a9a" stroke-width="1.6" fill="none"/>
</svg>
<div class="cert" style="left:300px"><div class="badge"></div><h3>Certified Fertility<br>Massage Therapist</h3><p>Lorem ipsum dolor sit amet, consectetuer adipiscing elit,</p><div class="more">VIEW DETAILS</div></div>
<div class="cert" style="left:628px"><div class="badge"></div><h3>Certified Infant Massage<br>Therapist~Instructor</h3><p>Lorem ipsum dolor sit amet, consectetuer adipiscing elit,</p><div class="more">VIEW DETAILS</div></div>
<div class="cert" style="left:957px"><div class="badge" style="left:104px;width:74px;border-radius:50%;background:#e6dccc;border-color:#5a4a3a"></div><h3>Certified Massage Doula</h3><p>Lorem ipsum dolor sit amet, consectetuer adipiscing elit,</p><div class="more">VIEW DETAILS</div></div>

<!-- FREE COURSE -->
<div class="photo" style="left:0;top:2890px;width:1200px;height:522px;background:linear-gradient(120deg,#dfe2e3,#f4f5f5 40%,#c9cdcd 70%,#eceeee)" role="img" aria-label="Jade face roller, spa stones and pine sprigs on a white tray"></div>
<div class="abs" style="left:161px;top:2975px;width:395px;height:350px;background:var(--white)"></div>
<h2 class="abs" style="left:161px;top:3014px;width:395px;text-align:center;font:400 33px 'Quicksand',sans-serif;color:var(--blue)">TAKE A <b style="font-weight:700">FREE</b> COURSE</h2>
<p class="abs" style="left:161px;top:3092px;width:395px;text-align:center;font-size:20px;line-height:32px;color:#555">Click here to get started<br>today &amp; try our <span style="color:var(--ink)">FREE</span><br>online course!</p>
<div class="btn" style="left:288px;top:3232px;width:140px;height:47px">READ MORE</div>

<!-- FAQ -->
<h2 class="section-title" style="top:3478px;font-size:33px">FREQUENTLY ASKED QUESTIONS</h2>
<p class="abs" style="left:0;top:3533px;width:1200px;text-align:center;font-size:12px;color:#555">ABOUT OUR ONLINE CONTINUING EDUCATION COURSES</p>

<div class="faq" style="left:228px;top:3621px"><div class="q-icon">?</div><h4>I am currently in massage school. Can I start taking your pregnancy massage course now so when I become licensed I'll be ready to work on pregnant women?</h4><p style="top:56px">Yes. Many massage therapy students begin taking continuing education courses as they near the end of their schooling.</p></div>
<div class="faq" style="left:633px;top:3621px"><div class="q-icon">?</div><h4>Do I have to be a licensed massage therapist to take your courses?</h4><p style="top:36px">While our courses are designed as continuing education for licensed and/or certified massage therapists, a non-licensed person may take them for their personal use.</p></div>
<div class="faq-rule" style="left:228px;top:3729px;width:345px"></div>
<div class="faq-rule" style="left:633px;top:3729px;width:345px"></div>
<div class="faq" style="left:228px;top:3749px"><div class="q-icon">?</div><h4>Are your online courses downloadable to my computer?</h4><p style="top:22px">No. You must be logged in on our website to view the course materials</p></div>
<div class="faq" style="left:633px;top:3749px"><div class="q-icon">?</div><h4>Will your online courses work on my phone, tablet, or other device?</h4><p style="top:34px">Yes. Since technology continues its rapid pace forward, it is impossible for us to provide a current and complete list of all devices on which our courses will work. We invite you to take our free sample course, Shoulder Dysfunction,</p></div>
<div class="faq-rule" style="left:228px;top:3874px;width:345px"></div>
<div class="faq-rule" style="left:633px;top:3874px;width:345px"></div>
<div class="faq" style="left:228px;top:3896px"><div class="q-icon">?</div><h4>Can I log in and out while taking an online course, or do I have to take it all at once?</h4><p style="top:22px">You are able to log in and out as much as you need while taking a course.</p></div>
<div class="faq" style="left:633px;top:3896px"><div class="q-icon">?</div><h4 style="top:6px">How do I print an additional certificate?</h4><p style="top:38px">You can log into your account and print additional certificates,</p></div>
<div class="btn" style="left:529px;top:4008px;width:140px;height:48px">READ MORE</div>

<!-- FOOTER -->
<footer class="abs footer"></footer>
<div class="flink" style="left:178px;top:4200px">Home</div>
<div class="flink" style="left:178px;top:4229px">Courses</div>
<div class="flink" style="left:178px;top:4257px">Guidelines</div>
<div class="flink" style="left:178px;top:4286px">Faqs</div>
<div class="flink" style="left:279px;top:4200px">Policies</div>
<div class="flink" style="left:279px;top:4229px">Contact</div>
<div class="flink" style="left:279px;top:4257px">About</div>
<div class="logo" style="left:478px;top:4232px;color:var(--white)">Quillory Points Institute</div>
<p class="abs" style="left:840px;top:4203px;width:140px;font-size:10.5px;line-height:14px;color:var(--white)">© Copyright 2022 Quillory Points Institute. All rights reserved.</p>
<div class="btn" style="left:526px;top:4283px;width:121px;height:45px;background:#555555;box-shadow:none;font-size:16px">LOGIN</div>

</body>
</html>
```